Safety Work Area Signage to keep people away from work zone

We would like to create a simple design that will include our logo and phone number, 'work area', and 'caution / cuidado' (please see a mock-up of the intended design in the uploaded files). Please provide multiple options. We would like a Professional look for the poster as it is meant for safety. Poster Size to be: 18.16" X 23.10"

Target Market(s)

General Public on Construction Sites

Font styles to use
Serif

Requirements
Must have
• see mock-ups in uploaded files
Nice to have
• Simple Design, Professional Look

```html
<!DOCTYPE html>
<html lang="en">
<head>
<meta charset="utf-8">
<title>Hartley &amp; Reed – Caution Signage</title>
<link rel="stylesheet" href="https://fonts.googleapis.com/css2?family=Oswald:wght@700&family=Archivo:wght@700&family=Montserrat:wght@700&family=Merriweather:wght@700;900&display=swap">
<style>
  :root {
    --red: #ee3338;
    --navy: #2b3483;
    --white: #ffffff;
    --shadow: #b8b8b8;
    --caution-font: "Oswald", sans-serif;
    --body-font: "Archivo", sans-serif;
    --phone-font: "Montserrat", sans-serif;
    --brand-font: "Merriweather", serif;
  }
  * { box-sizing: border-box; margin: 0; padding: 0; }
  html, body { width: 1200px; height: 994px; overflow: hidden; background: var(--white); }
  .artboard {
    position: relative;
    width: 1287px;
    height: 1066px;
    transform: scale(0.9324);
    transform-origin: 0 0;
  }

  /* ---------- Sign ---------- */
  .sign {
    position: absolute;
    top: 54px;
    width: 567px;
    height: 720px;
    box-shadow: 9px 9px 6px var(--shadow);
    overflow: hidden;
  }
  .sign--light { left: 62px; background: var(--white); border: 1px solid #222; }
  .sign--dark  { left: 666px; background: var(--navy); border: 1px solid #222; }

  .hazard-band {
    position: absolute;
    left: 0; right: 0;
    height: 164px;
  }
  .hazard-band--top { top: 22px; }
  .hazard-band--bottom { top: 534px; }
  .sign--light .hazard-band {
    background: repeating-linear-gradient(110deg, var(--red) 0 24px, var(--white) 24px 52px);
  }
  .sign--dark .hazard-band {
    background: repeating-linear-gradient(110deg, var(--red) 0 24px, var(--navy) 24px 52px);
  }

  .notice {
    position: absolute;
    top: 208px; left: 0; right: 0;
    height: 244px;
    padding: 3px;
    display: grid;
    grid-template-columns: 238px 1fr;
    gap: 5px;
  }
  .sign--light .notice { background: var(--navy); }
  .sign--dark  .notice { background: var(--red); }

  .brand-panel {
    background: var(--white);
    display: flex;
    align-items: center;
    justify-content: center;
    text-align: center;
  }
  .brand-name {
    font-family: var(--brand-font);
    font-weight: 900;
    font-size: 34px;
    line-height: 1.15;
    color: var(--navy);
  }

  .message-panel { display: flex; flex-direction: column; }
  .caution {
    height: 84px;
    font-family: var(--caution-font);
    font-weight: 700;
    font-size: 76px;
    line-height: 84px;
    letter-spacing: 1px;
    text-align: center;
    color: var(--white);
  }
  .restriction {
    flex: 1;
    margin: 0 2px 2px 0;
    background: var(--white);
    display: flex;
    align-items: center;
    justify-content: center;
    text-align: center;
    font-family: var(--body-font);
    font-weight: 700;
    font-size: 34px;
    line-height: 44px;
  }
  .sign--light .restriction { color: var(--navy); }
  .sign--dark  .restriction { color: var(--red); }

  .phone {
    position: absolute;
    top: 464px; left: 0; right: 0;
    text-align: center;
    font-family: var(--phone-font);
    font-weight: 700;
    font-size: 38px;
    letter-spacing: 2px;
    line-height: 60px;
  }
  .sign--light .phone { color: var(--red); }
  .sign--dark  .phone { color: var(--white); }

  /* ---------- Tape banner ---------- */
  .tape {
    position: absolute;
    left: 0; right: 0;
    top: 840px;
    height: 226px;
    background: repeating-linear-gradient(125deg, var(--red) 0 30px, var(--white) 30px 62px);
  }
  .tape-label {
    position: absolute;
    left: 424px;
    top: 72px;
    width: 438px;
    height: 82px;
    background: var(--white);
    display: flex;
    align-items: center;
    justify-content: center;
    gap: 16px;
    color: var(--navy);
    font-family: var(--brand-font);
  }
  .tape-brand {
    font-weight: 900;
    font-size: 24px;
    line-height: 1.05;
    text-align: left;
  }
  .tape-divider { width: 2px; height: 60px; background: var(--navy); }
  .tape-trade {
    font-weight: 700;
    font-size: 27px;
    line-height: 1.05;
    text-align: center;
  }
</style>
</head>
<body>
<div class="artboard">

  <section class="sign sign--light">
    <div class="hazard-band hazard-band--top"></div>
    <div class="notice">
      <div class="brand-panel"><p class="brand-name">Hartley<br>&amp; Reed, Inc.</p></div>
      <div class="message-panel">
        <h1 class="caution">CAUTION</h1>
        <p class="restriction">AUTHORISED<br>PERSONEL<br>ONLY</p>
      </div>
    </div>
    <p class="phone">(555) 014-2738</p>
    <div class="hazard-band hazard-band--bottom"></div>
  </section>

  <section class="sign sign--dark">
    <div class="hazard-band hazard-band--top"></div>
    <div class="notice">
      <div class="brand-panel"><p class="brand-name">Hartley<br>&amp; Reed, Inc.</p></div>
      <div class="message-panel">
        <h1 class="caution">CAUTION</h1>
        <p class="restriction">AUTHORISED<br>PERSONEL<br>ONLY</p>
      </div>
    </div>
    <p class="phone">(555) 014-2738</p>
    <div class="hazard-band hazard-band--bottom"></div>
  </section>

  <section class="tape">
    <div class="tape-label">
      <p class="tape-brand">Hartley<br>&amp; Reed, Inc.</p>
      <span class="tape-divider"></span>
      <p class="tape-trade">General<br>Contractors</p>
    </div>
  </section>

</div>
</body>
</html>
```